Silver Brook Decorators Banner

Create a banner that displays and reinforces Silver Brook Decorators’ brand identity while promoting our interior painting services. The banner will be displayed at indoor venues through the winter. The design should be clean, professional, and visually recognizable to both new and returning customers. See attached design brief & logo source files.

```html
<!DOCTYPE html>
<html lang="en">
<head>
<meta charset="utf-8">
<title>Silver Brook Decorators – Interior Painting Banner</title>
<link rel="stylesheet" href="https://fonts.googleapis.com/css2?family=Archivo:ital,wght@0,800;0,900;1,800&family=Montserrat:wght@800&family=Oswald:wght@700&family=Open+Sans:ital,wght@0,400;0,700;1,800&display=swap">
<style>
  :root {
    --brand-green: #75995a;
    --charcoal: #4c4e4b;
    --paper: #f8f8f8;
    --backdrop: #e7e9ea;
  }
  * { margin: 0; padding: 0; box-sizing: border-box; }
  html, body {
    width: 1200px; height: 840px; overflow: hidden;
    background: var(--backdrop);
  }
  .banner {
    position: absolute; left: 30px; top: 195px;
    width: 1140px; height: 450px;
    background: var(--paper);
    overflow: hidden;
    box-shadow: 0 4px 18px rgba(0,0,0,.12);
  }
  .brand-name {
    position: absolute; left: 40px; top: 28px;
    font-family: "Montserrat", sans-serif; font-weight: 800;
    color: var(--brand-green);
    font-size: 62px; line-height: 1.02; letter-spacing: 1px;
    text-transform: uppercase;
  }
  .service-band {
    position: absolute; left: 0; top: 190px; width: 100%; height: 112px;
    background: var(--charcoal);
  }
  .service-title {
    position: absolute; left: 38px; top: 4px;
    font-family: "Oswald", sans-serif; font-weight: 700;
    font-size: 92px; line-height: 1.1; color: var(--paper);
    letter-spacing: 1px;
  }
  .trust-badge {
    position: absolute; left: 835px; top: -6px; width: 258px; height: 238px;
    background: var(--brand-green);
    border: 4px solid var(--paper); border-top: none;
    border-radius: 0 0 42px 42px;
    color: var(--paper); text-align: center;
    font-family: "Archivo", sans-serif;
  }
  .trust-badge .lead { font-weight: 900; font-size: 56px; line-height: 1; margin-top: 36px; }
  .trust-badge .sub { font-weight: 800; font-size: 19px; margin-top: 4px; }
  .trust-badge .since {
    display: flex; align-items: center; justify-content: center; gap: 10px;
    font-weight: 800; font-size: 26px; line-height: 1.1;
  }
  .trust-badge .since::before, .trust-badge .since::after {
    content: ""; width: 50px; height: 3px; background: var(--paper);
  }
  .trust-badge .year { font-weight: 900; font-size: 76px; line-height: 1; }
  .service-list {
    position: absolute; left: 0; top: 302px; width: 100%; height: 76px;
    background: var(--brand-green);
    display: flex; align-items: center; gap: 26px; padding-left: 36px;
    list-style: none;
  }
  .service-list li {
    display: flex; align-items: center; gap: 4px;
    font-family: "Archivo", sans-serif; font-style: italic; font-weight: 800;
    font-size: 38px; color: var(--charcoal);
  }
  .service-list svg { width: 32px; height: 32px; }
  .contact-row {
    position: absolute; left: 0; top: 378px; width: 100%; height: 72px;
    display: flex; align-items: center; padding-left: 38px;
    color: var(--charcoal);
  }
  .cta {
    font-family: "Open Sans", sans-serif; font-size: 19px; line-height: 1.1;
    width: 180px;
  }
  .cta em { font-weight: 800; }
  .contact-item {
    display: flex; align-items: center; gap: 8px;
    font-family: "Archivo", sans-serif; font-weight: 800;
  }
  .website { font-size: 36px; margin-left: 18px; }
  .phone { font-size: 38px; margin-left: 36px; }
  .contact-item svg { width: 30px; height: 30px; }
</style>
</head>
<body>
  <main class="banner">
    <h1 class="brand-name">Silver Brook<br>Decorators</h1>

    <section class="service-band">
      <h2 class="service-title">INTERIOR PAINTING</h2>
    </section>

    <aside class="trust-badge">
      <div class="lead">Trusted</div>
      <div class="sub">Local Professionals</div>
      <div class="since">Since</div>
      <div class="year">2005</div>
    </aside>

    <ul class="service-list">
      <li><svg viewBox="0 0 32 32"><rect x="3" y="7" width="22" height="22" rx="3" fill="none" stroke="#4c4e4b" stroke-width="3"/><path d="M8 17l6 6L29 4" fill="none" stroke="#4c4e4b" stroke-width="3.5" stroke-linecap="round"/></svg>Walls</li>
      <li><svg viewBox="0 0 32 32"><rect x="3" y="7" width="22" height="22" rx="3" fill="none" stroke="#4c4e4b" stroke-width="3"/><path d="M8 17l6 6L29 4" fill="none" stroke="#4c4e4b" stroke-width="3.5" stroke-linecap="round"/></svg>Ceilings</li>
      <li><svg viewBox="0 0 32 32"><rect x="3" y="7" width="22" height="22" rx="3" fill="none" stroke="#4c4e4b" stroke-width="3"/><path d="M8 17l6 6L29 4" fill="none" stroke="#4c4e4b" stroke-width="3.5" stroke-linecap="round"/></svg>Trim</li>
      <li><svg viewBox="0 0 32 32"><rect x="3" y="7" width="22" height="22" rx="3" fill="none" stroke="#4c4e4b" stroke-width="3"/><path d="M8 17l6 6L29 4" fill="none" stroke="#4c4e4b" stroke-width="3.5" stroke-linecap="round"/></svg>Cabinets</li>
      <li><svg viewBox="0 0 32 32"><rect x="3" y="7" width="22" height="22" rx="3" fill="none" stroke="#4c4e4b" stroke-width="3"/><path d="M8 17l6 6L29 4" fill="none" stroke="#4c4e4b" stroke-width="3.5" stroke-linecap="round"/></svg>Drywall Repair</li>
    </ul>

    <footer class="contact-row">
      <p class="cta">BOOK YOUR<br><em>FREE</em> ESTIMATE</p>
      <span class="contact-item website">
        <svg viewBox="0 0 30 30"><circle cx="15" cy="15" r="13" fill="#75995a"/><ellipse cx="15" cy="15" rx="6" ry="13" fill="none" stroke="#f8f8f8" stroke-width="1.6"/><path d="M2 15h26M5 8h20M5 22h20" stroke="#f8f8f8" stroke-width="1.6"/></svg>
        www.silverbrookdecor.com
      </span>
      <span class="contact-item phone">
        <svg viewBox="0 0 30 30"><path d="M7 3l5 1 2 6-3 3c1.5 3 3.5 5 6 6l3-3 6 2 1 5-3 3C13 26 4 17 4 6z" fill="#75995a"/></svg>
        (555) 014-2760
      </span>
    </footer>
  </main>
</body>
</html>
```